develop our online residential property development appraisal service

This project requires a detailed WordPress design to represent a new digital residential property development consultancy business. At its heart it will have a number of different products that essentially advise customers of the potential value and feasibility of developing their residential site into multiple townhouses, units, apartments, etc... This will be accompanied by explaining the considerations of residential property development.

We aim to navigate and break down this complex area and provide our customers with the tools, knowledge, control and power to 'unlock the value' in their property.

REFERENCE DOCUMENTS:
1. Detailed solution requirements please refer to the attached 'wordpressdesignrequirements'
2. Logo files, style guide and colour pallet please refer to the attached 'KRMV.zip'
3. Site Map refer to attached 'wordpressdesignsitemap'

Reason: Additional information provided so extending period for designs to take into account.

Target Market(s)

The site will appeal to professional service providers; accountants, financial planners, lawyers, etc…

Industry/Entity Type

Residential

Font styles to use
Sans Serif
Other font styles liked:
• Similar to the logo font, slim line and simple

Requirements
Must have
• The logo, style and colour palette provided in the attached 'KRMV.zip' files
• Satisfy the intent of the 'wordpressdesignrequirements'
• Present as an online-centric business
• Clean, crisp and modern design
• Predominant use of white as a background contrasted with the colours provided in the colour palette
Nice to have
• Use of the following WordPress business themes is encouraged but not mandatory:
• 1. Tovu
• 2. Pilmu
• 3. Vomi
Should not have
• Overt references to Australia

```html
<!DOCTYPE html>
<html lang="en">
<head>
<meta charset="utf-8">
<title>KRMV – Residential Site Value Advisory</title>
<link href="https://fonts.googleapis.com/css2?family=Raleway:wght@400;500;600&family=Open+Sans:wght@400;600&display=swap" rel="stylesheet">
<style>
:root{
  --green:#2aa866;
  --green-dark:#1f9455;
  --teal:#1e9a80;
  --teal-light:#1aa9a0;
  --teal-deep:#17877a;
  --ink:#333;
  --muted:#666;
  --line:#ddd;
  --white:#fff;
}
*{margin:0;padding:0;box-sizing:border-box}
html,body{width:727px;height:1200px;overflow:hidden;background:var(--white)}
body{position:relative;font-family:"Open Sans",sans-serif;color:var(--ink)}
.abs{position:absolute}
.head{font-family:"Raleway",sans-serif}

/* header */
.brand{left:85px;top:14px;display:flex;align-items:center;gap:8px}
.brand-name{font-family:"Raleway",sans-serif;font-size:34px;font-weight:400;color:var(--green);letter-spacing:1px}
.brand-divider{width:1px;height:42px;background:#ccc}
.brand-tag{font-family:"Raleway",sans-serif;font-size:12px;line-height:13px;color:#bbb}
.search{left:510px;top:38px;width:133px;height:18px;border:1px solid #bbb;border-radius:2px;font-size:6.5px;font-style:italic;color:#777;padding:4px 7px}
.search svg{position:absolute;right:6px;top:3px}

/* nav */
.nav{left:0;top:67px;width:727px;height:33px;background:linear-gradient(var(--green),var(--green-dark));display:flex;padding-left:77px}
.nav a{font-family:"Raleway",sans-serif;font-size:9.5px;font-weight:500;color:var(--white);text-decoration:none;padding:0 8px;line-height:33px;border-right:1px solid rgba(255,255,255,.25)}
.nav a:last-child{border:0}

/* hero */
.hero{left:0;top:100px;width:727px;height:278px;background:linear-gradient(135deg,#3c5a8a 0%,#2c4470 40%,#6a6080 70%,#a07a40 100%)}
.hero-box{left:197px;top:165px;width:357px;height:112px;background:rgba(30,35,45,.75);text-align:center;color:var(--white)}
.hero-kicker{font-family:"Raleway",sans-serif;font-size:13.5px;font-weight:500;margin-top:22px}
.hero-title{font-family:"Raleway",sans-serif;font-size:21px;font-weight:500;margin-top:2px}
.hero-btn{display:inline-block;margin-top:4px;background:var(--green);color:var(--white);font-family:"Raleway",sans-serif;font-size:9.5px;font-weight:600;padding:7px 10px}
.arrow{top:205px}

/* intro band */
.band{left:0;top:378px;width:727px;height:142px;background:var(--teal)}
.band-col{top:409px;width:175px;color:var(--white)}
.band-col h2{font-family:"Raleway",sans-serif;font-size:12.5px;font-weight:400;margin-bottom:6px}
.band-col p{font-size:6.3px;line-height:11px;opacity:.9}
.band-col .more{display:block;font-family:"Raleway",sans-serif;font-size:7.5px;margin-top:6px;opacity:.7}

/* reports & opportunities */
.section-title{font-family:"Raleway",sans-serif;font-size:15px;color:var(--green);font-weight:400}
.report{left:84px;width:290px;display:flex;gap:13px}
.report-img{width:83px;height:71px;flex:none}
.report h3{font-family:"Raleway",sans-serif;font-size:9.5px;font-weight:400;margin-bottom:3px}
.report p{font-size:6.3px;line-height:11px;color:var(--muted)}
.report .more{font-size:7.3px;color:var(--green);margin-top:3px;display:block}
.opp{left:400px;width:220px;display:flex;gap:9px}
.opp h3{font-family:"Raleway",sans-serif;font-size:9px;font-weight:400;margin-bottom:4px}
.opp p{font-size:6.3px;line-height:11px;color:var(--muted)}
.rule{left:0;top:790px;width:727px;height:1px;background:var(--line)}

/* development cards */
.dev-title{left:88px;top:816px;font-family:"Raleway",sans-serif;font-size:14.5px;color:var(--ink)}
.card{top:846px;width:172px}
.card-img{width:172px;height:75px}
.card h3{font-family:"Raleway",sans-serif;font-size:9.5px;font-weight:400;color:var(--green);margin:7px 0 3px 2px}
.card p{font-size:6.3px;line-height:11px;color:var(--muted);margin-left:2px}
.card .more{font-size:7.3px;color:var(--ink);display:block;margin:4px 0 0 2px}

/* footer */
.footer{left:0;top:1016px;width:727px;height:184px;background:linear-gradient(var(--teal-light),var(--teal-deep))}
.f-col{top:1043px;color:var(--white)}
.f-col h4{font-family:"Raleway",sans-serif;font-size:9.5px;font-weight:400;margin-bottom:5px}
.f-col a{display:block;font-size:7.3px;line-height:15.3px;color:var(--white);text-decoration:none}
.f-sep{top:1040px;width:1px;height:86px;background:rgba(255,255,255,.15)}
.socials{left:385px;top:1112px;display:flex;gap:9px}
.socials span{width:14px;height:14px;border-radius:50%;background:var(--white);display:block}
.f-rule{left:85px;top:1160px;width:557px;height:1px;background:rgba(255,255,255,.15)}
.copy{left:85px;top:1173px;font-size:6.3px;color:rgba(255,255,255,.5)}
</style>
</head>
<body>

<header>
  <div class="abs brand">
    <span class="brand-name">KRMV</span>
    <span class="brand-divider"></span>
    <span class="brand-tag">Residential Site<br>Value Advisory</span>
  </div>
  <div class="abs search">Search here
    <svg width="10" height="10" viewBox="0 0 10 10"><circle cx="4" cy="4" r="3" fill="none" stroke="#888" stroke-width="1.2"/><line x1="6.2" y1="6.2" x2="9" y2="9" stroke="#888" stroke-width="1.4"/></svg>
  </div>
</header>

<nav class="abs nav">
  <a>Email Collection Page</a><a>Property Report Page A</a><a>Property Report Page B</a><a>Property Report Page C</a><a>About Us</a><a>Contact Us</a>
</nav>

<section>
  <div class="abs hero" role="img" aria-label="Modern apartment buildings lit at dusk"></div>
  <svg class="abs arrow" style="left:58px" width="24" height="50" viewBox="0 0 24 50"><polyline points="22,2 2,25 22,48" fill="none" stroke="#fff" stroke-width="2"/></svg>
  <svg class="abs arrow" style="left:648px" width="24" height="50" viewBox="0 0 24 50"><polyline points="2,2 22,25 2,48" fill="none" stroke="#fff" stroke-width="2"/></svg>
  <div class="abs hero-box">
    <div class="hero-kicker">PHASELLUS FELIS DOLOR SCELERISQUE</div>
    <div class="hero-title">ETIAM NULLA MASSA PHARETRA</div>
    <span class="hero-btn">Request Property Report</span>
  </div>
</section>

<section>
  <div class="abs band"></div>
  <div class="abs band-col" style="left:84px"><h2>WHO ARE WE</h2><p>Integer congue augue et malesuada iaculis ipsum dui aliquet felis at cursus magna nisl nec elit Praesent elementum elit at tellus nec ultricies sit amet porttitor mattis enim In massa libero interdum nec</p><span class="more">LEARN MORE</span></div>
  <div class="abs band-col" style="left:279px"><h2>WHAT DO WE DO?</h2><p>Integer congue augue et malesuada iaculis ipsum dui aliquet felis at cursus magna nisl nec elit Praesent elementum elit at tellus nec ultricies sit amet porttitor mattis enim In massa libero interdum nec</p><span class="more">LEARN MORE</span></div>
  <div class="abs band-col" style="left:472px"><h2>HOW DO WE DO IT?</h2><p>Integer congue augue et malesuada iaculis ipsum dui aliquet felis at cursus magna nisl nec elit Praesent elementum elit at tellus nec ultricies sit amet porttitor mattis enim In massa libero interdum nec</p><span class="more">LEARN MORE</span></div>
</section>

<section>
  <h2 class="abs section-title" style="left:85px;top:552px">Property Report Pages</h2>
  <div class="abs report" style="top:585px">
    <div class="report-img" role="img" aria-label="Advisors meeting with a client in an office" style="background:linear-gradient(135deg,#d8dde2,#9aa4ae)"></div>
    <div><h3>Integer augue malesuada</h3><p>iaculis ipsum dui aliquet felis at cursus magna nisl nec elit Praesent elementum elit at tellus nec ultricies sit amet porttitor mattis enim In massa libero interdum nec interdum vel blandit sed nulla In ullamcorper est eget tempor cursus</p><span class="more">Read More</span></div>
  </div>
  <div class="abs report" style="top:678px">
    <div class="report-img" role="img" aria-label="Two people in a business consultation" style="background:linear-gradient(135deg,#3a302c,#c9c4bf)"></div>
    <div><h3>Donec dictum lectus</h3><p>iaculis ipsum dui aliquet felis at cursus magna nisl nec elit Praesent elementum elit at tellus nec ultricies sit amet porttitor mattis enim In massa libero interdum nec interdum vel blandit sed nulla In ullamcorper est eget tempor cursus</p><span class="more">Read More</span></div>
  </div>

  <h2 class="abs section-title" style="left:401px;top:552px">Opportunities We Provides</h2>
  <div class="abs opp" style="top:580px"><svg width="15" height="15" viewBox="0 0 16 16"><circle cx="8" cy="8" r="8" fill="var(--teal)"/><polyline points="4,8.5 7,11 12,5" fill="none" stroke="#fff" stroke-width="2"/></svg><div><h3>Altricies sit amet porttitor mattis</h3><p>enim In massa libero interdum nec interdum vel blandit sed</p></div></div>
  <div class="abs opp" style="top:622px"><svg width="15" height="15" viewBox="0 0 16 16"><circle cx="8" cy="8" r="8" fill="var(--teal)"/><polyline points="4,8.5 7,11 12,5" fill="none" stroke="#fff" stroke-width="2"/></svg><div><h3>Cum sociis natoque penatibus et magnis</h3><p>Cras a ante vitae enim iaculis aliquam Mauris nunc quam ven enatis nec euismod sit amet egestas placerat</p></div></div>
  <div class="abs opp" style="top:673px"><svg width="15" height="15" viewBox="0 0 16 16"><circle cx="8" cy="8" r="8" fill="var(--teal)"/><polyline points="4,8.5 7,11 12,5" fill="none" stroke="#fff" stroke-width="2"/></svg><div><h3>Lorem ipsum dolor sit amet</h3><p>enim In massa libero interdum nec interdum vel blandit sed</p></div></div>
  <div class="abs opp" style="top:711px"><svg width="15" height="15" viewBox="0 0 16 16"><circle cx="8" cy="8" r="8" fill="var(--teal)"/><polyline points="4,8.5 7,11 12,5" fill="none" stroke="#fff" stroke-width="2"/></svg><div><h3>Mauris vel lacus vitae felis</h3><p>enim In massa libero interdum nec interdum vel blandit sed</p></div></div>
</section>

<div class="abs rule"></div>

<section>
  <h2 class="abs dev-title">Property Development</h2>
  <div class="abs card" style="left:87px"><div class="card-img" role="img" aria-label="Business meeting around a table" style="background:linear-gradient(135deg,#5a4a40,#b8bcc4)"></div><h3>Donec dictum lectus</h3><p>iaculis ipsum dui aliquet felis at cursus magna nisl nec elit Praesent elementum elit at tellus nec ultr</p><span class="more">Read More</span></div>
  <div class="abs card" style="left:279px"><div class="card-img" role="img" aria-label="Building under construction with cranes" style="background:linear-gradient(#3f7fd0,#9a8a70)"></div><h3>Mauris vel lacus vitae felis</h3><p>iaculis ipsum dui aliquet felis at cursus magna nisl nec elit Praesent elementum elit at tellus nec ultr</p><span class="more">Read More</span></div>
  <div class="abs card" style="left:470px"><div class="card-img" role="img" aria-label="Site workers in safety vests reviewing plans" style="background:linear-gradient(135deg,#8a6a50,#c8d070)"></div><h3>Proin nulla arcu nonummy luctus</h3><p>iaculis ipsum dui aliquet felis at cursus magna nisl nec elit Praesent elementum elit at tellus nec ultr</p><span class="more">Read More</span></div>
</section>

<footer>
  <div class="abs footer"></div>
  <div class="abs f-col" style="left:89px"><h4>COMPANY</h4><a>About Us</a><a>Social Media Integration</a><a>Email Collection Page</a><a>Property Development Overview</a></div>
  <div class="abs f-sep" style="left:218px"></div>
  <div class="abs f-col" style="left:243px"><h4>RESOURCES</h4><a>Property Report Page A</a><a>Property Report Page B</a><a>Property Report Page C</a><a>Contact Us</a></div>
  <div class="abs f-sep" style="left:354px"></div>
  <div class="abs f-col" style="left:385px"><h4>CONTACT US</h4><a>48 Larkmoor Lane Suite 3 Westfield 20417</a><a>555.014.2290</a><a>hello@krmvsites.com</a></div>
  <div class="abs socials"><span></span><span></span><span></span><span></span></div>
  <div class="abs f-rule"></div>
  <div class="abs copy">© 2015 Company Name  All right reserved  Term of Use</div>
</footer>

</body>
</html>
```